Auto Detailing Facility Needs Facebook Cover Photo

Looking for a beautiful Facebook cover photo using our logo and a photo, including our business information. Does not have to use the photo provided but the logo must be in there. I want an eye-catching cover photo that promotes the luxury brand.

Website: www.glossbayauto.com
Phone: 555-555-0147
Address: 412 Lower Maple Rd Unit B-3 Millbrook, CT 02091

Industry/Entity Type

Automotive

Colors

Designer to choose colors to be used in the design.

```html
<!DOCTYPE html>
<html lang="en">
<head>
<meta charset="utf-8">
<title>Gloss Bay – Cover Photo Variations</title>
<link rel="stylesheet" href="https://fonts.googleapis.com/css2?family=Barlow:wght@300;400;600;700&display=swap">
<style>
  :root {
    --stage: #333333;
    --white: #ffffff;
    --ink: #111111;
    --navy: #06087f;
    --slate: #4a4a4a;
    --brand-dark: #333333;
  }
  * { margin: 0; padding: 0; box-sizing: border-box; }
  html, body { width: 1200px; height: 1200px; overflow: hidden; }
  body {
    background: var(--stage);
    font-family: "Barlow", sans-serif;
  }
  .canvas {
    position: relative;
    width: 1200px;
    height: 1200px;
  }
  .cover {
    position: absolute;
    left: 166px;
    width: 867px;
    height: 330px;
    display: block;
  }
  .cover--light { top: 54px;  --panel: var(--white); --text: var(--ink);   --brand: var(--brand-dark); }
  .cover--navy  { top: 434px; --panel: var(--navy);  --text: var(--white); --brand: var(--white); }
  .cover--slate { top: 815px; --panel: var(--slate); --text: var(--white); --brand: var(--white); }

  .cover__panel { fill: var(--panel); }
  .cover__title {
    fill: var(--text);
    font-family: "Barlow", sans-serif;
    font-weight: 700;
    font-size: 20px;
    letter-spacing: 0.4px;
  }
  .cover__tagline {
    fill: var(--text);
    font-family: "Barlow", sans-serif;
    font-weight: 400;
    font-size: 19px;
  }
  .cover__contact {
    fill: var(--text);
    font-family: "Barlow", sans-serif;
    font-weight: 600;
    font-size: 7.2px;
  }
  .cover__icon {
    fill: none;
    stroke: var(--text);
    stroke-width: 0.7;
  }
  .cover__brand {
    fill: var(--brand);
    font-family: "Barlow", sans-serif;
    font-weight: 400;
    font-size: 8.5px;
    letter-spacing: 1px;
  }
</style>
</head>
<body>
<main class="canvas">

  <svg class="cover cover--light" viewBox="0 0 723 275" aria-label="Gloss Bay cover, white version">
    <defs>
      <linearGradient id="photo-tone" x1="0" y1="0" x2="1" y2="1">
        <stop offset="0" stop-color="#14171f"/>
        <stop offset="0.5" stop-color="#262b36"/>
        <stop offset="0.72" stop-color="#5d6577"/>
        <stop offset="1" stop-color="#101319"/>
      </linearGradient>
    </defs>
    <rect class="cover__photo" width="723" height="275" fill="url(#photo-tone)" role="img" aria-label="Photo of a white sports car in a dark garage"/>
    <polygon class="cover__panel" points="0,0 100,0 316,222 242,275 0,275"/>
    <polygon class="cover__panel" points="389,0 707,0 532,142"/>
    <polygon class="cover__panel" points="407,275 440,275 608,154 592,154"/>
    <polygon class="cover__panel" points="650,275 723,275 723,206"/>
    <text class="cover__brand" x="548" y="87" text-anchor="middle">GLOSS BAY</text>
    <text class="cover__title" x="118" y="133" text-anchor="middle">GLOSS BAY</text>
    <text class="cover__tagline" x="118" y="155" text-anchor="middle">auto care</text>
    <rect class="cover__icon" x="35.5" y="211" width="3" height="6" rx="0.6"/>
    <text class="cover__contact" x="52" y="217">555-555-0147</text>
    <rect class="cover__icon" x="34.5" y="223.5" width="5" height="3.5"/>
    <path class="cover__icon" d="M34.5 223.5 L37 225.5 L39.5 223.5"/>
    <text class="cover__contact" x="52" y="228">www.glossbayauto.com</text>
    <path class="cover__icon" d="M37 240 C35 237.5 35 236 35 235.5 A2 2 0 0 1 39 235.5 C39 236 39 237.5 37 240 Z"/>
    <text class="cover__contact" x="52" y="239">412 Lower Maple Rd Unit B-3 Millbrook, CT 02091</text>
  </svg>

  <svg class="cover cover--navy" viewBox="0 0 723 275" aria-label="Gloss Bay cover, navy version">
    <rect class="cover__photo" width="723" height="275" fill="url(#photo-tone)" role="img" aria-label="Photo of a white sports car in a dark garage"/>
    <polygon class="cover__panel" points="0,0 100,0 316,222 242,275 0,275"/>
    <polygon class="cover__panel" points="389,0 707,0 532,142"/>
    <polygon class="cover__panel" points="407,275 440,275 608,154 592,154"/>
    <polygon class="cover__panel" points="650,275 723,275 723,206"/>
    <text class="cover__brand" x="548" y="87" text-anchor="middle">GLOSS BAY</text>
    <text class="cover__title" x="118" y="133" text-anchor="middle">GLOSS BAY</text>
    <text class="cover__tagline" x="118" y="155" text-anchor="middle">auto care</text>
    <rect class="cover__icon" x="35.5" y="211" width="3" height="6" rx="0.6"/>
    <text class="cover__contact" x="52" y="217">555-555-0147</text>
    <rect class="cover__icon" x="34.5" y="223.5" width="5" height="3.5"/>
    <path class="cover__icon" d="M34.5 223.5 L37 225.5 L39.5 223.5"/>
    <text class="cover__contact" x="52" y="228">www.glossbayauto.com</text>
    <path class="cover__icon" d="M37 240 C35 237.5 35 236 35 235.5 A2 2 0 0 1 39 235.5 C39 236 39 237.5 37 240 Z"/>
    <text class="cover__contact" x="52" y="239">412 Lower Maple Rd Unit B-3 Millbrook, CT 02091</text>
  </svg>

  <svg class="cover cover--slate" viewBox="0 0 723 275" aria-label="Gloss Bay cover, slate version">
    <rect class="cover__photo" width="723" height="275" fill="url(#photo-tone)" role="img" aria-label="Photo of a white sports car in a dark garage"/>
    <polygon class="cover__panel" points="0,0 100,0 316,222 242,275 0,275"/>
    <polygon class="cover__panel" points="389,0 707,0 532,142"/>
    <polygon class="cover__panel" points="407,275 440,275 608,154 592,154"/>
    <polygon class="cover__panel" points="650,275 723,275 723,206"/>
    <text class="cover__brand" x="548" y="87" text-anchor="middle">GLOSS BAY</text>
    <text class="cover__title" x="118" y="133" text-anchor="middle">GLOSS BAY</text>
    <text class="cover__tagline" x="118" y="155" text-anchor="middle">auto care</text>
    <rect class="cover__icon" x="35.5" y="211" width="3" height="6" rx="0.6"/>
    <text class="cover__contact" x="52" y="217">555-555-0147</text>
    <rect class="cover__icon" x="34.5" y="223.5" width="5" height="3.5"/>
    <path class="cover__icon" d="M34.5 223.5 L37 225.5 L39.5 223.5"/>
    <text class="cover__contact" x="52" y="228">www.glossbayauto.com</text>
    <path class="cover__icon" d="M37 240 C35 237.5 35 236 35 235.5 A2 2 0 0 1 39 235.5 C39 236 39 237.5 37 240 Z"/>
    <text class="cover__contact" x="52" y="239">412 Lower Maple Rd Unit B-3 Millbrook, CT 02091</text>
  </svg>

</main>
</body>
</html>
```